Business Card & Logo Design

Originally the brief was for a card only - I now think it's probably better to include a logo design as well. PLease add $200 to the Budget of $210, Apologies for the inconvenience for thaos that have already submitted designs.

Lantern Hollow Productions Pty Ltd is a video/dvd/ production company. Primarily corporate medium to high end. It's a one man operation that's been in business 20 years.

The name " Lantern Hollow" is a primarily a reference to Mathieu Corbelle film that's about film making. Shooting "Lantern Hollow" is also a technique employed by cinematographers to make scenes shot in daylight look like night.

See the design emphasising blue day/night tones but open to other ideas.

Main Text can either be Lantern Hollow Productions or Lantern Hollow.

Many thanks to all designers who submitted ideas for this brief.

Choosing between the designs was very difficult indeed.

I wish everyone the best and may the next job be yours!

Warren

• Text for card:
In Larger Print
Lantern Hollow Productions or Lantern Hollow
Warren Bellamy
In Smaller Print
Lantern Hollow Productions Pty Ltd.
17 Pelham Street
Corran Vale, TAS, 7261
P: 9734 2061
m: 0438 725 190
e: warrenbellamy@ostrafel.com

```html
<!DOCTYPE html>
<html lang="en">
<head>
<meta charset="utf-8">
<title>Lantern Hollow Productions – Business Card</title>
<link rel="stylesheet" href="https://fonts.googleapis.com/css2?family=Archivo:wght@400;600;800&display=swap">
<style>
  :root {
    --ink: #000000;
    --paper: #ffffff;
    --stage: #f4f4f4;
    --trim: #222222;
  }
  * { margin: 0; padding: 0; box-sizing: border-box; }
  html, body {
    width: 1200px;
    height: 901px;
    overflow: hidden;
    background: var(--stage);
    font-family: "Archivo", Arial, sans-serif;
  }
  .canvas {
    position: relative;
    width: 1200px;
    height: 901px;
  }
  .crop-marks {
    position: absolute;
    left: 330px;
    top: 45px;
    width: 540px;
    height: 810px;
  }
  .business-card {
    position: absolute;
    left: 390px;
    top: 105px;
    width: 420px;
    height: 690px;
    background: var(--paper);
    color: var(--ink);
    overflow: hidden;
    box-shadow: 0 2px 10px rgba(0,0,0,0.08);
  }
  .card-shapes {
    position: absolute;
    inset: 0;
  }
  .company-details {
    position: absolute;
    left: 26px;
    top: 30px;
    color: var(--paper);
    font-size: 15px;
    font-weight: 600;
    font-style: normal;
    line-height: 1.55;
  }
  .brand-lockup {
    position: absolute;
    left: 0;
    right: 0;
    top: 318px;
    display: flex;
    align-items: center;
    justify-content: center;
    gap: 10px;
  }
  .brand-mark {
    width: 22px;
    height: 22px;
    background: var(--ink);
  }
  .brand-name {
    font-size: 26px;
    font-weight: 800;
    letter-spacing: -0.5px;
    color: var(--ink);
  }
  .contact-block {
    position: absolute;
    right: 26px;
    bottom: 44px;
    text-align: right;
    color: var(--paper);
  }
  .contact-name {
    display: inline-block;
    font-size: 22px;
    font-weight: 600;
    text-transform: uppercase;
    padding-bottom: 3px;
    border-bottom: 2px solid var(--paper);
    margin-bottom: 14px;
  }
  .contact-line {
    font-size: 15px;
    font-weight: 600;
    line-height: 1.6;
  }
</style>
</head>
<body>
<main class="canvas">
  <svg class="crop-marks" viewBox="0 0 540 810" aria-hidden="true">
    <g stroke="var(--trim)" stroke-width="1.2">
      <line x1="60" y1="0" x2="60" y2="40"/>
      <line x1="0" y1="60" x2="40" y2="60"/>
      <line x1="480" y1="0" x2="480" y2="40"/>
      <line x1="500" y1="60" x2="540" y2="60"/>
      <line x1="60" y1="770" x2="60" y2="810"/>
      <line x1="0" y1="750" x2="40" y2="750"/>
      <line x1="480" y1="770" x2="480" y2="810"/>
      <line x1="500" y1="750" x2="540" y2="750"/>
    </g>
  </svg>

  <article class="business-card">
    <svg class="card-shapes" viewBox="0 0 420 690" aria-hidden="true">
      <polygon class="header-band" points="0,0 420,0 420,84 0,200" fill="var(--ink)"/>
      <polygon class="footer-band" points="0,690 140,540 420,540 420,690" fill="var(--ink)"/>
    </svg>

    <address class="company-details">
      Lantern Hollow Productions Pty Ltd.<br>
      17 Pelham Street<br>
      Corran Vale, TAS, 7261<br>
      P: 9734 2061
    </address>

    <div class="brand-lockup">
      <span class="brand-mark"></span>
      <span class="brand-name">Lantern Hollow Productions</span>
    </div>

    <div class="contact-block">
      <div class="contact-name">Warren Bellamy</div>
      <div class="contact-line">m: 0438 725 190</div>
      <div class="contact-line">e: warrenbellamy@ostrafel.com</div>
    </div>
  </article>
</main>
</body>
</html>
```